Business Card Design Project

We consult with hotels on setting rates and maximizing a revenue strategy

Industry/Entity Type

Business

Contact Information for Business Card

I am not sure what I want. Our company offers high level consulting to hotels around the country but we are also laid back. I would like something that is professional but also shows the laid back side

```html
<!DOCTYPE html>
<html lang="en">
<head>
<meta charset="utf-8">
<title>Harborline Revenue Advisors – Business Cards</title>
<link href="https://fonts.googleapis.com/css2?family=Open+Sans:wght@400;600;700&display=swap" rel="stylesheet">
<style>
  :root {
    --teal: #1f8a86;
    --teal-dark: #17706c;
    --ink: #2b2b2b;
    --muted: #555;
    --paper: #ffffff;
    --stage: #e9eaea;
    --faint: #eef1f1;
  }
  * { box-sizing: border-box; margin: 0; padding: 0; }
  html, body { width: 1200px; height: 1001px; overflow: hidden; }
  body {
    background: var(--stage);
    font-family: "Open Sans", Arial, sans-serif;
    color: var(--ink);
    position: relative;
  }
  .card {
    position: absolute;
    top: 150px;
    width: 400px;
    height: 700px;
    background: var(--paper);
    box-shadow: 0 2px 10px rgba(0,0,0,.12);
    overflow: hidden;
  }
  .card--front { left: 150px; }
  .card--back { left: 650px; }

  /* Front */
  .front-decor {
    position: absolute;
    top: 40px; left: 40px; right: 40px;
    height: 400px;
    background: linear-gradient(180deg, var(--faint), #f8f9f9);
  }
  .front-logo {
    position: absolute;
    right: 36px; bottom: 70px;
    display: flex; align-items: center; gap: 12px;
  }
  .logo-dot {
    width: 34px; height: 34px; border-radius: 50%;
    background: var(--teal);
  }
  .logo-name {
    font-weight: 700;
    font-size: 34px;
    color: var(--teal);
    letter-spacing: 1px;
  }
  .front-tag {
    position: absolute;
    right: 36px; bottom: 44px;
    font-size: 13px; color: var(--muted);
    letter-spacing: .5px;
  }

  /* Back */
  .back-band { position: absolute; top: 0; left: 0; width: 400px; height: 150px; }
  .company {
    position: absolute; top: 20px; right: 26px;
    text-align: right; color: #fff;
    font-size: 18px; line-height: 1.2;
  }
  .back-logo {
    position: absolute; top: 190px; left: 60px;
    display: flex; align-items: center; gap: 10px;
  }
  .back-logo .logo-name { font-size: 26px; }
  .back-logo .logo-dot { width: 26px; height: 26px; }
  .person { position: absolute; top: 330px; left: 40px; }
  .person-name { font-size: 24px; font-weight: 600; }
  .person-title { font-size: 18px; color: var(--muted); margin-top: 2px; }
  .contacts { position: absolute; top: 420px; left: 40px; list-style: none; }
  .contacts li {
    display: flex; align-items: center; gap: 12px;
    font-size: 17px; margin-bottom: 14px; color: var(--ink);
  }
  .contacts li.web { color: var(--teal); }
  .icon {
    width: 22px; height: 22px; border-radius: 50%;
    background: var(--teal); flex: none;
    display: flex; align-items: center; justify-content: center;
  }
  .back-foot {
    position: absolute; bottom: 0; left: 0; right: 0; height: 26px;
    background: var(--teal);
  }
</style>
</head>
<body>

  <section class="card card--front">
    <div class="front-decor" role="img" aria-label="Faint large decorative brand symbol area"></div>
    <div class="front-logo">
      <span class="logo-dot"></span>
      <span class="logo-name">HARBORLINE</span>
    </div>
    <div class="front-tag">Revenue Advisors</div>
  </section>

  <section class="card card--back">
    <svg class="back-band" viewBox="0 0 400 150" aria-hidden="true">
      <path d="M0 0 H400 V120 H250 Q200 120 170 90 L140 60 H0 Z" fill="var(--teal)"/>
      <path d="M0 60 H140 L170 90 Q200 120 250 120 H400" fill="none" stroke="var(--teal-dark)" stroke-width="3"/>
    </svg>
    <div class="company">HARBORLINE<br>Revenue Advisors<br>LLC</div>

    <div class="back-logo">
      <span class="logo-dot"></span>
      <span class="logo-name">HARBORLINE</span>
    </div>

    <div class="person">
      <div class="person-name">Dana Whitlock</div>
      <div class="person-title">Regional Revenue Manager</div>
    </div>

    <ul class="contacts">
      <li><span class="icon"><svg width="12" height="12" viewBox="0 0 12 12"><path d="M2 1l2 0 1 3-1.5 1a7 7 0 0 0 3.5 3.5L8 7l3 1v2a1 1 0 0 1-1 1A9 9 0 0 1 1 2a1 1 0 0 1 1-1z" fill="#fff"/></svg></span>: 503-555-0142</li>
      <li><span class="icon"><svg width="12" height="12" viewBox="0 0 12 12"><rect x="2" y="1" width="8" height="4" fill="#fff"/><rect x="1" y="5" width="10" height="5" rx="1" fill="#fff"/></svg></span>: 503-555-0187</li>
      <li><span class="icon"><svg width="12" height="12" viewBox="0 0 12 12"><rect x="1" y="3" width="10" height="7" fill="#fff"/><path d="M1 3l5 4 5-4" fill="none" stroke="var(--teal)" stroke-width="1"/></svg></span>: dana@harborlinera.com</li>
      <li class="web"><span class="icon"><svg width="12" height="12" viewBox="0 0 12 12"><circle cx="6" cy="6" r="4.5" fill="none" stroke="#fff"/><path d="M1.5 6h9M6 1.5v9" stroke="#fff"/></svg></span>: www.harborlinera.com</li>
    </ul>

    <div class="back-foot"></div>
  </section>

</body>
</html>
```